Create the ONLY Supplement line for Male Entrepreneurs! (Veltro Prime MD)

I need a label designed for a new supplement brand that I am launching.

There are five products so need a design that I can simply change the wording for each individual product

The brand name is called veltro prime MD. The focus is male entrepreneurial health.

Target audience is men 35 to 55.

Concepts: the healthier you are in body the more money you will make in business.

Concept to copy: I want to make a clean minimalistic label mimicking Dallamore MD (google it and you'll see what I mean)

Target Market(s)

male entrepreneurs 35-55

Industry/Entity Type

Health Supplement

Colors

Designer to choose colors to be used in the design.

Requirements
Must have
• Modern classy design, similar to Dallamore MD.
Nice to have
• Highlight that the supplement is Doctor Approved.
Should not have
• No loud colors. Present it as high class.

```html
<!DOCTYPE html>
<html lang="en">
<head>
<meta charset="utf-8">
<title>Veltro Prime MD – Supplement Labels</title>
<link rel="stylesheet" href="https://fonts.googleapis.com/css2?family=Cormorant+Garamond:wght@500&family=Montserrat:wght@300;400&display=swap">
<style>
  :root {
    --page: #ffffff;
    --silver: #a7a8ac;
    --silver-dark: #8e8f93;
    --silver-line: #c9cacd;
    --label-white: #f3f3f1;
    --label-blue: #d3dfe7;
    --figure-light: rgba(255,255,255,0.55);
  }
  * { box-sizing: border-box; margin: 0; padding: 0; }
  html, body { width: 1200px; height: 1200px; overflow: hidden; background: var(--page); }
  body { position: relative; font-family: "Montserrat", sans-serif; color: var(--silver); }

  .brand-lockup { position: absolute; left: 128px; top: 118px; width: 690px; }
  .brand-row { display: flex; align-items: flex-end; gap: 22px; }
  .brand-dot { width: 44px; height: 44px; border-radius: 50%; background: var(--silver); margin-bottom: 6px; }
  .brand-name {
    font-family: "Cormorant Garamond", serif; font-weight: 500;
    font-size: 74px; line-height: 1; color: var(--silver); letter-spacing: 0.5px;
  }
  .brand-rule { height: 2px; margin-top: 8px; background: linear-gradient(90deg, var(--silver) 0%, var(--silver-line) 70%, rgba(201,202,205,0) 100%); }
  .brand-tagline { margin: 12px 0 0 85px; font-size: 29px; font-weight: 400; color: var(--silver-dark); letter-spacing: 0.3px; }

  .label-set { position: absolute; left: 195px; top: 470px; display: flex; gap: 50px; }
  .label {
    position: relative; width: 380px; height: 520px; overflow: hidden;
    border-radius: 4px; padding: 90px 0 0 30px;
  }
  .label--omega { background: var(--label-white); }
  .label--multi { background: var(--label-blue); }
  .label-figure {
    position: absolute; inset: 0;
    background: radial-gradient(ellipse 45% 60% at 58% 55%, var(--figure-light), rgba(255,255,255,0) 75%);
  }
  .label-content { position: relative; }
  .label-brand { display: flex; align-items: flex-end; gap: 10px; }
  .label-brand .brand-dot { width: 22px; height: 22px; margin-bottom: 4px; }
  .label-brand .brand-name { font-size: 36px; }
  .label-rule { height: 2px; background: var(--silver-line); margin-right: 0; }
  .label-brand + .label-rule { margin-top: 4px; }
  .label-tagline { margin: 8px 0 0 40px; font-size: 15px; color: var(--silver-dark); }
  .cert-badge {
    position: absolute; right: 44px; top: 70px; width: 52px; height: 52px;
    border-radius: 50%; border: 2px solid var(--silver); background: rgba(255,255,255,0.5);
  }
  .product-name {
    margin: 110px 0 8px 40px; font-family: "Cormorant Garamond", serif; font-weight: 500;
    font-size: 34px; color: var(--silver); line-height: 1;
  }
  .product-type { margin: 10px 0 8px 40px; font-size: 15px; color: var(--silver-dark); }
  .product-count { margin: 12px 0 0 40px; font-size: 15px; color: var(--silver-dark); }
  .label-rule--indent { margin-left: 40px; }
</style>
</head>
<body>
  <header class="brand-lockup">
    <div class="brand-row">
      <span class="brand-dot"></span>
      <span class="brand-name">Veltro Prime MD</span>
    </div>
    <div class="brand-rule"></div>
    <p class="brand-tagline">male entrepreneurial health</p>
  </header>

  <main class="label-set">
    <section class="label label--omega">
      <div class="label-figure" role="img" aria-label="Faint line illustration of a male torso"></div>
      <div class="label-content">
        <div class="label-brand">
          <span class="brand-dot"></span>
          <span class="brand-name">Veltro Prime MD</span>
        </div>
        <div class="label-rule"></div>
        <p class="label-tagline">male entrepreneurial health</p>
        <span class="cert-badge" aria-label="Certification badge"></span>
        <h2 class="product-name">Omega 3</h2>
        <div class="label-rule label-rule--indent"></div>
        <p class="product-type">Dietary Supplement</p>
        <div class="label-rule label-rule--indent"></div>
        <p class="product-count">90 softgel</p>
      </div>
    </section>

    <section class="label label--multi">
      <div class="label-figure" role="img" aria-label="Faint line illustration of a male torso"></div>
      <div class="label-content">
        <div class="label-brand">
          <span class="brand-dot"></span>
          <span class="brand-name">Veltro Prime MD</span>
        </div>
        <div class="label-rule"></div>
        <p class="label-tagline">male entrepreneurial health</p>
        <span class="cert-badge" aria-label="Certification badge"></span>
        <h2 class="product-name">Multivit Male</h2>
        <div class="label-rule label-rule--indent"></div>
        <p class="product-type">Dietary Supplement</p>
        <div class="label-rule label-rule--indent"></div>
        <p class="product-count">90 softgel</p>
      </div>
    </section>
  </main>
</body>
</html>
```